Willow Creek Haven website design

To create 2 pages (a front page and sub page) for a health/spiritual website. I have a logo, and was thinking of incorporating Greek temple columns in the design or something similar, but open to other ideas.

The design should suit mobile devices with limited screen space also.

Industry/Entity Type

Health

Number of Pages Required

1 page

```html
<!DOCTYPE html>
<html lang="en">
<head>
<meta charset="utf-8">
<title>Willow Creek Haven</title>
<link href="https://fonts.googleapis.com/css2?family=Questrial&family=Cormorant+Garamond:wght@500;600&display=swap" rel="stylesheet">
<style>
:root{
  --sky:#9fd6e3;
  --ink:#3a474d;
  --teal:#25a3c0;
  --teal-dark:#1b8aa5;
  --white:#ffffff;
  --rule:#c6e6ee;
  --footer-top:#52626f;
  --footer-bottom:#2f3b37;
}
*{margin:0;padding:0;box-sizing:border-box}
html,body{width:1200px;height:2647px;overflow:hidden}
body{position:relative;background:var(--sky);font-family:"Questrial",sans-serif;color:var(--ink)}
.abs{position:absolute}

/* header */
.brand-mark{left:81px;top:18px;width:56px;height:56px;background:#1e1e1e}
.brand-name{left:152px;top:30px;font-size:24px;font-weight:400;color:#2b2f33;letter-spacing:.3px}
.social{top:24px;width:30px;height:30px;border-radius:50%}
.social.s1{left:948px;background:#2f5f9e}
.social.s2{left:984px;background:#3aa0d8}
.social.s3{left:1020px;background:#c8412f}

/* hero */
.hero{left:0;top:109px;width:1200px;height:675px;
  background:linear-gradient(180deg,#2f6da6 0%,#6f9fc7 22%,#b7cfe0 38%,#5a7fa5 52%,#1d3a5c 72%,#0c1a2c 100%)}
.nav{left:120px;top:138px;width:965px;height:65px;background:rgba(255,255,255,.55);
  box-shadow:0 6px 10px rgba(0,0,0,.35);display:flex;justify-content:center;align-items:center;gap:30px}
.nav a{font-size:23px;color:#1d2a35;text-decoration:none}
.hero-caption{left:340px;top:366px;width:620px;text-align:center;color:var(--white);font-size:19px;line-height:21px;font-weight:700;text-shadow:0 1px 2px rgba(0,0,0,.4)}
.arrow{top:387px;width:42px;height:42px}
.arrow.prev{left:76px}
.arrow.next{left:1082px}

/* intro */
.intro-title{left:0;width:1200px;top:832px;text-align:center;font-family:"Cormorant Garamond",serif;font-size:29px;font-weight:600}
.intro-sub{left:0;width:1200px;top:868px;text-align:center;font-family:"Cormorant Garamond",serif;font-size:22px;font-weight:500}

.feature-img{top:964px;width:222px;height:123px}
.feature-text{top:1113px;width:210px;font-size:14px;line-height:19.5px}
.btn-more{top:1251px;width:94px;height:32px;background:var(--teal);color:var(--white);font-size:12px;
  display:flex;align-items:center;justify-content:center;box-shadow:0 2px 2px rgba(0,0,0,.25)}
.col-rule{top:964px;width:1px;height:293px;background:var(--rule)}

.story-img{position:absolute}
.story-text{font-size:14px;line-height:19px}

/* call to action */
.cta{left:171px;top:1915px;width:854px;height:81px;background:var(--teal);border-radius:8px;
  box-shadow:0 3px 5px rgba(0,0,0,.25)}
.cta-text{left:198px;top:1943px;font-size:20px;color:var(--white)}
.cta-btn{left:868px;top:1931px;width:133px;height:47px;border:2px solid var(--white);color:var(--white);
  font-size:21px;font-weight:700;display:flex;align-items:center;justify-content:center}

/* footer */
.footer{left:0;top:2060px;width:1200px;height:587px;
  background:linear-gradient(180deg,var(--footer-top) 0%,#5b6b76 45%,#4a5a56 78%,var(--footer-bottom) 100%)}
.footer-col{top:2226px;width:190px;color:var(--white)}
.footer-col h3{font-size:19px;font-weight:400;margin-bottom:16px}
.footer-col p,.footer-col li{font-size:13.5px;line-height:18.5px;list-style:none}
.footer-col p+p{margin-top:12px}
.field{left:867px;width:158px;height:28px;border:2px solid var(--white);color:var(--white);font-size:11px;padding:5px 6px}
.submit{left:867px;top:2363px;width:67px;height:21px;border:1px solid var(--white);color:var(--white);font-size:10px;padding:3px 5px}
.footer-rule{left:175px;top:2594px;width:850px;height:1px;background:rgba(255,255,255,.6)}
.copyright{left:0;width:1200px;top:2616px;text-align:center;color:var(--white);font-size:13px}
</style>
</head>
<body>

<header>
  <div class="abs brand-mark"></div>
  <div class="abs brand-name">Willow Creek Haven</div>
  <span class="abs social s1" aria-label="Social link"></span>
  <span class="abs social s2" aria-label="Social link"></span>
  <span class="abs social s3" aria-label="Social link"></span>
</header>

<section>
  <div class="abs hero" role="img" aria-label="Silhouette of a person meditating at the water's edge under a blue evening sky"></div>
  <nav class="abs nav">
    <a href="#">Home</a><a href="#">Aboutus</a><a href="#">Foundations Program</a><a href="#">Services</a><a href="#">Contact</a>
  </nav>
  <p class="abs hero-caption">Lorem Ipsum is simply dummy text of the printing and typesetting industry. Lorem Ipsum has been the industry's standard dummy text ever since the 1500s,</p>
  <svg class="abs arrow prev" viewBox="0 0 42 42"><circle cx="21" cy="21" r="18" fill="none" stroke="#fff" stroke-width="3"/><path d="M24 12 L15 21 L24 30" fill="none" stroke="#fff" stroke-width="3"/></svg>
  <svg class="abs arrow next" viewBox="0 0 42 42"><circle cx="21" cy="21" r="18" fill="none" stroke="#fff" stroke-width="3"/><path d="M18 12 L27 21 L18 30" fill="none" stroke="#fff" stroke-width="3"/></svg>
</section>

<section>
  <h2 class="abs intro-title">Lorem Ipsum</h2>
  <p class="abs intro-sub">Lorem Ipsum is simply dummy text of the printing and typeset</p>

  <div class="abs feature-img" style="left:175px;background:radial-gradient(circle,#6fa8e8 0%,#2c4f8c 40%,#141c36 100%)" role="img" aria-label="Glowing brain surrounded by light orbits"></div>
  <div class="abs feature-img" style="left:494px;background:linear-gradient(180deg,#7fb3de 0%,#d9c7e6 45%,#2f6fae 70%,#1a3e6e 100%)" role="img" aria-label="Person meditating on the shore at dusk"></div>
  <div class="abs feature-img" style="left:805px;background:radial-gradient(circle,#e8f6f7 0%,#6cc4cf 40%,#1b5f6c 100%)" role="img" aria-label="Figure standing in a field of glowing light"></div>

  <div class="abs col-rule" style="left:443px"></div>
  <div class="abs col-rule" style="left:755px"></div>

  <p class="abs feature-text" style="left:175px">Lorem Ipsum is simply dummy text of the printing and typeset-ting industry. Lorem Ipsum has been the industry's standard dummy text ever since the 1500s,</p>
  <p class="abs feature-text" style="left:494px">Lorem Ipsum is simply dummy text of the printing and typeset-ting industry. Lorem Ipsum has been the industry's standard dummy text ever since the 1500s,</p>
  <p class="abs feature-text" style="left:805px;top:1111px">Lorem Ipsum is simply dummy text of the printing and typeset-ting industry. Lorem Ipsum has been the industry's standard dummy text ever since the 1500s,</p>

  <a class="abs btn-more" style="left:175px">Read more</a>
  <a class="abs btn-more" style="left:494px">Read more</a>
  <a class="abs btn-more" style="left:805px">Read more</a>
</section>

<section>
  <div class="story-img" style="left:175px;top:1401px;width:289px;height:170px;background:linear-gradient(180deg,#1a1530 0%,#4a2a4a 45%,#c8b8c8 75%,#3a2a3a 100%)" role="img" aria-label="Glowing triangle above clouds in a starry sky"></div>
  <p class="abs story-text" style="left:498px;top:1399px;width:531px">Lorem Ipsum is simply dummy text of the printing and typesetting industry. Lorem Ipsum has been the industry's standard dummy text ever since the 1500s, when an unknown printer took a galley of type and scrambled it to make a type specimen book. It has survived not only five centuries, but also the leap into electronic type-setting, remaining essentially unchanged.Lorem Ipsum is simply dummy text of the printing and typesetting industry. Lorem Ipsum has been the industry's standard dummy text ever since the 1500s, when an unknown printer took a galley of type and scrambled it to make a type specimen book. It has survived not only five cen-turies, but also the leap into electronic typesetting, remaining essentially un electronic typesetting, remaining essentially unchanged.</p>

  <p class="abs story-text" style="left:175px;top:1639px;width:515px">Lorem Ipsum is simply dummy text of the printing and typesetting industry. Lorem Ipsum has been the industry's standard dummy text ever since the 1500s, when an unknown printer took a galley of type and scrambled it to make a type specimen book. It has survived not only five centuries, but also the leap into electronic type-setting, remaining essentially unchanged.Lorem Ipsum is simply dummy text of the printing and typesetting industry. Lorem Ipsum has been the industry's standard dummy text ever since the 1500s, when an unknown printer took a galley of type and scrambled it to make a type specimen book. It has survived not only five cen-turies, but also the leap into electronic typesetting, remaining essentially un electronic typesetting, remaining essentially unchanged.</p>
  <div class="story-img" style="left:724px;top:1643px;width:301px;height:175px;background:radial-gradient(circle,#8a5a3a 0%,#4a2a1a 55%,#1a0e08 100%)" role="img" aria-label="Cupped hands holding stones engraved with hopeful words"></div>
</section>

<section>
  <div class="abs cta"></div>
  <p class="abs cta-text">Lorem Ipsum is simply dummy text of</p>
  <a class="abs cta-btn">Join us</a>
</section>

<footer>
  <div class="abs footer" role="img" aria-label="Ruined Greek temple columns against a hazy sky"></div>
  <div class="abs footer-col" style="left:175px">
    <h3>About us</h3>
    <p>Lorem Ipsum is simply dummy text of the printing and typesetting industry. Lorem Ipsum has been the industry's standard dummy text ever since the 1500s,</p>
    <p>Lorem Ipsum is simply dummy text of the printing and typesetting industry. Lorem Ipsum has been the industry's standard dummy text ever since the 1500s,</p>
  </div>
  <div class="abs footer-col" style="left:450px">
    <h3>Usefull Links</h3>
    <ul><li>Sit avertas dero</li><li>taserto yaendala mi</li><li>aseay</li><li>mertase deles neory</li><li>kastreas</li><li>verode fase laisuase</li><li>avertelero ferose</li><li>taserto yndolase</li><li>mertaleras neory</li><li>verode fertase</li></ul>
  </div>
  <div class="abs footer-col" style="left:662px;top:2228px">
    <h3>Services</h3>
    <ul><li>Sit avertas dero</li><li>taserto yaendala mi</li><li>aseay</li><li>mertase deles neory</li><li>kastreas</li><li>verode fase laisuase</li><li>avertelero ferose</li><li>taserto yndolase</li><li>mertaeleras neory</li><li>verode fertase</li></ul>
  </div>
  <div class="abs footer-col" style="left:867px;top:2228px">
    <h3>News letter</h3>
  </div>
  <div class="abs field" style="top:2275px">Name</div>
  <div class="abs field" style="top:2319px">E-mail</div>
  <div class="abs submit">Submit</div>
  <div class="abs footer-rule"></div>
  <p class="abs copyright">@ Privacy policy 2016</p>
</footer>

</body>
</html>
```